Flyer-Design für Neueröffnung eines Online-Shops
Zielgruppe
Ich verkaufe Online Lebensmittel, die normalerweise entsorgt werden, da das Mindesthaltbarkeitsdatum (MHD ) entweder in Kürze abläuft oder bereits überschritten ist, obwohl diese noch genießbar sind.
Der Fokus liegt auf nicht kühlbedürftige Ware wie Getränke, Süßwaren, Cerealien, Konserven, Gewürze, Getreidetrockenprodukte. Hinzu kommen Sonderposten aus Geschäftsauflösungen, Überproduktionen usw.
Das Ziel ist es, die Lebensmittelverschwendung zu reduzieren und der Bevölkerung, genießbare Lebensmittel zu einem geringen Preis anzubieten.
Die beiden Hauptzielgruppen sind;
1. Umweltbewusste Personen, die die Reduzierung der Lebensmittelverschwendung unterstützen wollen
2. Personen aus dem Niedriglohnsektor, die jeden Euro 'zweimal' umdrehen müssen und sich keine Markenware leisten können.
Aufgabenstellung
Der Onlineshop startet im Januar, das bedeutet der Onlineshop ist noch nicht bekannt. Daher soll der Flyer einem sofort ins Auge fallen. Jedoch soll auf dem Flyer nicht erwähnt werden, dass es sich um einen 'Neueröffnung' handelt.
Jedoch fahre ich eine Eröffnungsaktion, die jedoch als 'Januar' Special' oder Neujahrsspecial' o.ä. betitelt werden soll. Nämlich 'versandkostenfreie Lieferung ab 10€ Warenwert*'
*gilt für Bestellungen bis zum 31.01.18
Folgende Inhalte sollten im Design vorkommen:
Das Logo, der Slogan ' Verschwendung reduzieren, Ersparnis maximieren', die Domain 'www.kor-tibu.de' + der Hinweis auf die versandkostenfreie Lieferung am 10€ Warenwert im Januar.
Folgende Inhalte sind optional:
Stichwörter wie 'nachhaltig', 'umweltbewusst', 'bis zu 70% Ersparnis', '82kg Lebensmittel werden jährlich pro Person entsorgt',
Als Farbton sollte grün im Vordergrund stehen, gerne in zwei verschiedenen Helligkeitsstufen. Als Kontrastfarben wären Ideen rot( für den Rabatt/Ersparnis und da es sich um MHD nahe Lebensmittel handelt ) und schwarz oder weiß.
Der Flyer wird im A5 Hochformat gedruckt ( Querformat bei Bedarf auch möglich ). Dicke = voraussichtlich 300gr (alternativ 250gr ), 2-seitig
Ich werde das Logo und eine erste Skizze von einer Flyervorlage. Die Flyervorlage soll jedoch nur als Unterstützung für die Farbgebung dienen. Bitte die Designs unabhängig davon gestalten und diese evtl als kleine 'Hilfe' nutzen.
Da das Thema recht erklärungsbedürftig ist, ist meine Idee auf der Rückseite eine Art Begriffsklärung zu erstellen. Eine Vorlage für den Inhalt habe ich erstellt und wird ebenfalls hochgeladen. Jedoch soll die Begriffsklärung nicht einfach runtergeschrieben werden sondern kreativ eingebaut/verpackt werden ( z.B. Sprechblasen oder Emojis, Cliparts o.ä. )
Der Kunde soll sofort sehen, dass es darum geht die Lebensmittelverschwendung zu reduzieren und im gleichen Zuge genießb..

```html
<!DOCTYPE html>
<html lang="de">
<head>
<meta charset="utf-8">
<title>Flyer Rückseite – Begriffsklärung</title>
<link rel="stylesheet" href="https://fonts.googleapis.com/css2?family=Roboto:wght@400;700;900&display=swap">
<style>
  :root {
    --bg: #e6e6e6;
    --paper: #ffffff;
    --green: #2f9a4e;
    --band: #4a4a4c;
    --white: #ffffff;
  }
  * { box-sizing: border-box; margin: 0; padding: 0; }
  html, body { width: 1200px; height: 900px; overflow: hidden; }
  body {
    background: var(--bg);
    font-family: "Roboto", Arial, sans-serif;
    display: flex; align-items: center; justify-content: center;
  }
  .flyer {
    position: relative;
    width: 594px; height: 840px;
    background: var(--paper);
    box-shadow: 0 6px 24px rgba(0,0,0,.12);
    overflow: hidden;
  }
  .bubble {
    position: absolute;
    left: 24px; right: 24px;
    background: var(--green);
    border-radius: 26px;
    color: var(--white);
    padding: 10px;
    z-index: 2;
  }
  .bubble-inner {
    border: 2px dashed rgba(255,255,255,.9);
    border-radius: 18px;
    height: 100%;
    padding: 18px 24px;
    position: relative;
  }
  .bubble h2 {
    font-weight: 700; font-size: 20px; line-height: 1.2;
    margin-bottom: 8px;
  }
  .bubble p { font-size: 15.5px; line-height: 1.4; }
  .tail { position: absolute; top: 100%; width: 60px; height: 44px; }
  .tail-left { left: 36px; }
  .tail-right { right: 70px; }
  .bubble-mhd { top: 26px; height: 220px; }
  .bubble-eat { top: 298px; height: 180px; }
  .bubble-diff { top: 530px; height: 244px; }
  .bubble-diff p { font-size: 14.5px; line-height: 1.35; }
  .url-band {
    position: absolute; left: 0; bottom: 0; width: 100%; height: 58px;
    z-index: 1;
  }
  .url-band svg { position: absolute; inset: 0; width: 100%; height: 100%; }
  .url {
    position: absolute; right: 24px; bottom: 8px;
    font-weight: 900; font-size: 34px; color: var(--white);
    letter-spacing: .5px;
  }
</style>
</head>
<body>
  <div class="flyer">
    <section class="bubble bubble-mhd">
      <div class="bubble-inner">
        <h2>Was bedeutet MHD nahe Lebensmittel &amp; Sonderposten?</h2>
        <p>Bei MHD nahe Lebensmitteln handelt es sich um Ware, bei denen das Mindesthaltbarkeitsdatum entweder in Kürze ansteht und bereits abgelaufen ist. Sonderposten sind Waren aus u.a. Geschäftsauflösungen und Insolvenzen, Produktionsüberhängen und Fehlproduktionen</p>
      </div>
      <svg class="tail tail-left" viewBox="0 0 60 44"><path d="M0 0 L0 44 L50 0 Z" fill="var(--green)"/><path d="M10 6 L10 30 L38 6" fill="none" stroke="#fff" stroke-width="2" stroke-dasharray="6 4"/></svg>
    </section>

    <section class="bubble bubble-eat">
      <div class="bubble-inner">
        <h2>Kann man abgelaufene Lebensmittel noch essen?</h2>
        <p>Nach Ablauf des Mindesthaltbarkeitsdatums sind viele Lebensmittel noch genießbar. Vorausgesetzt sie sind ungeöffnet und wurden richtig gelagert. Wenn jedoch das Verbrauchsdatum überschritten ist, sollten diese Lebensmittel nicht mehr verzehrt werden.</p>
      </div>
      <svg class="tail tail-right" viewBox="0 0 60 44"><path d="M10 0 L60 44 L60 0 Z" fill="var(--green)"/><path d="M22 6 L50 30 L50 6" fill="none" stroke="#fff" stroke-width="2" stroke-dasharray="6 4"/></svg>
    </section>

    <section class="bubble bubble-diff">
      <div class="bubble-inner">
        <h2>Was ist der Unterschied zwischen Mindesthaltbarkeitsdatum und Verbrauchsdatum?</h2>
        <p>Das Mindesthaltbarkeitsdatum gibt an, bis zu welchem Zeitpunkt ein Lebensmittel unter angemessenen Aufbewahrungsbedingungen seine spezifischen Eigenschaften (u.a. Qualität, Farbe, Geschmack) behält. Nach Ablauf des Verbrauchsdatum dürfen Lebensmittel nicht mehr verzehrt werden, da eine Gefährdung der Gesundheit nicht mehr auszuschließen ist.</p>
      </div>
      <svg class="tail tail-left" viewBox="0 0 60 44"><path d="M0 0 L0 44 L50 0 Z" fill="var(--green)"/><path d="M10 6 L10 30 L38 6" fill="none" stroke="#fff" stroke-width="2" stroke-dasharray="6 4"/></svg>
    </section>

    <footer class="url-band">
      <svg viewBox="0 0 594 58" preserveAspectRatio="none"><path d="M60 58 L110 0 L594 0 L594 58 Z" fill="var(--band)"/></svg>
      <span class="url">www.kor-tibu.de</span>
    </footer>
  </div>
</body>
</html>
```